Building sign design

We need a sign design for the front of our automotive workshop building. The sign needs to fit the colours of our building and company. (black, red, grey and white). The sign needs to stand out and be a modern.

Sign is to replace the red Pennock Cells sign. 2900mmx2900mm.
Company logo attached (Highgear).
Also photos of old sign and building.

Sign needs to feature Highgear logo at top and what we do below.

-Warrant of Fitness
-Vehicle Servicing
-All Mechanical Repairs
-Tyres & Wheel Alignments
-Batteries & Diagnostics
-Automotive Parts
-Vehicle Sales.

Also needs a large "WOF" somewhere on sign.

And contact details at bottom of sign.
48 Tamsin Road
07 542 3917

```html
<!DOCTYPE html>
<html lang="en">
<head>
<meta charset="utf-8">
<title>Highgear Total Automotive – Building Sign</title>
<link rel="stylesheet" href="https://fonts.googleapis.com/css2?family=Anton&family=Barlow+Condensed:ital,wght@1,800&family=Krona+One&display=swap">
<style>
  :root {
    --sign-black: #060606;
    --sign-red: #e31e24;
    --sign-red-deep: #b5161b;
    --sign-grey: #7d7e82;
    --sign-white: #ffffff;
    --page-bg: #ffffff;
  }
  html, body {
    margin: 0;
    padding: 0;
    width: 934px;
    height: 1200px;
    overflow: hidden;
    background: var(--page-bg);
  }
  .canvas {
    position: relative;
    width: 934px;
    height: 1200px;
  }
  .sign {
    position: absolute;
    left: 27px;
    top: 160px;
    width: 880px;
    height: 880px;
    display: block;
    filter: drop-shadow(0 2px 6px rgba(0,0,0,0.25));
  }
  .brand-name { font-family: "Krona One", sans-serif; fill: var(--sign-red); }
  .brand-tagline { font-family: "Krona One", sans-serif; fill: var(--sign-white); }
  .wof-title { font-family: "Anton", sans-serif; fill: var(--sign-white); }
  .service-label { font-family: "Krona One", sans-serif; fill: var(--sign-white); font-size: 25px; }
  .contact-line { font-family: "Barlow Condensed", sans-serif; font-style: italic; font-weight: 800; fill: var(--sign-black); }
  .hex { fill: var(--sign-red); }
  .hex-shade { fill: var(--sign-red-deep); }
  .icon { fill: none; stroke: var(--sign-white); stroke-width: 2.4; stroke-linecap: round; stroke-linejoin: round; }
  .icon-solid { fill: var(--sign-white); }
  .leader { stroke: var(--sign-white); stroke-width: 3; }
</style>
</head>
<body>
<main class="canvas">
  <svg class="sign" viewBox="0 0 880 880" xmlns="http://www.w3.org/2000/svg">
    <defs>
      <linearGradient id="red-sweep" x1="0" y1="0" x2="1" y2="1">
        <stop offset="0" stop-color="#ee2a2c"/>
        <stop offset="1" stop-color="#b8161b"/>
      </linearGradient>
      <polygon id="hex-shape" points="-28,0 -14,-25 14,-25 28,0 14,25 -14,25"/>
    </defs>

    <!-- sign face -->
    <rect class="sign-face" x="0" y="0" width="880" height="880" fill="var(--sign-white)"/>
    <rect class="sign-panel" x="9" y="11" width="860" height="752" fill="var(--sign-black)"/>

    <!-- top stripe -->
    <polygon points="9,11 462,11 451,22 9,22" fill="var(--sign-red)"/>
    <polygon points="462,11 869,11 869,30 445,30" fill="var(--sign-grey)"/>
    <rect x="9" y="11" width="445" height="11" fill="var(--sign-red)"/>

    <!-- brand -->
    <text class="brand-name" x="70" y="131" font-size="80" textLength="740" lengthAdjust="spacingAndGlyphs">HIGHGEAR</text>
    <text class="brand-tagline" x="167" y="176" font-size="26" textLength="544" lengthAdjust="spacing">TOTAL AUTOMOTIVE</text>

    <!-- WOF -->
    <polygon points="228,301 308,301 308,308 236,308" fill="var(--sign-red)"/>
    <polygon points="240,312 308,312 308,319 248,319" fill="var(--sign-red)"/>
    <text class="wof-title" x="318" y="321" font-size="122" textLength="243" lengthAdjust="spacingAndGlyphs">WOF</text>
    <polygon points="570,301 654,301 646,308 570,308" fill="var(--sign-red)"/>
    <polygon points="570,312 642,312 634,319 570,319" fill="var(--sign-red)"/>

    <!-- services list -->
    <g class="services">
      <g transform="translate(0,386)">
        <line class="leader" x1="9" y1="0" x2="90" y2="0"/>
        <use href="#hex-shape" x="113" class="hex"/>
        <g transform="translate(113,0)">
          <rect class="icon" x="-11" y="-9" width="18" height="18" rx="2"/>
          <polyline class="icon" points="-7,0 -2,5 11,-10"/>
        </g>
        <text class="service-label" x="163" y="10" textLength="433" lengthAdjust="spacing">Warrant of Fitness</text>
      </g>
      <g transform="translate(0,441)">
        <line class="leader" x1="9" y1="0" x2="90" y2="0"/>
        <use href="#hex-shape" x="113" class="hex"/>
        <g transform="translate(113,0)">
          <line class="icon" x1="-14" y1="-12" x2="-14" y2="12"/>
          <line class="icon" x1="14" y1="-12" x2="14" y2="12"/>
          <line class="icon" x1="-14" y1="8" x2="14" y2="8"/>
          <path class="icon-solid" d="M-9,2 L-7,-5 L7,-5 L9,2 L9,5 L-9,5 Z"/>
        </g>
        <text class="service-label" x="163" y="10" textLength="388" lengthAdjust="spacing">Vehicle Servicing</text>
      </g>
      <g transform="translate(0,496)">
        <line class="leader" x1="9" y1="0" x2="90" y2="0"/>
        <use href="#hex-shape" x="113" class="hex"/>
        <g transform="translate(113,0)">
          <line class="icon" x1="-10" y1="10" x2="9" y2="-9" stroke-width="3.2"/>
          <line class="icon" x1="-10" y1="-10" x2="10" y2="10" stroke-width="3.2"/>
          <circle class="icon" cx="-11" cy="-11" r="3.5"/>
          <circle class="icon" cx="-11" cy="11" r="3.5"/>
        </g>
        <text class="service-label" x="163" y="10" textLength="513" lengthAdjust="spacing">All Mechanical Repairs</text>
      </g>
      <g transform="translate(0,551)">
        <line class="leader" x1="9" y1="0" x2="90" y2="0"/>
        <use href="#hex-shape" x="113" class="hex"/>
        <g transform="translate(113,0)">
          <circle class="icon" cx="2" cy="0" r="12"/>
          <circle class="icon" cx="2" cy="0" r="5"/>
          <line class="icon" x1="-16" y1="-4" x2="-11" y2="-4"/>
          <line class="icon" x1="-16" y1="4" x2="-11" y2="4"/>
        </g>
        <text class="service-label" x="163" y="10" textLength="593" lengthAdjust="spacing">Tyres &amp; Wheel Alignments</text>
      </g>
      <g transform="translate(0,606)">
        <line class="leader" x1="9" y1="0" x2="90" y2="0"/>
        <use href="#hex-shape" x="113" class="hex"/>
        <g transform="translate(113,0)">
          <rect class="icon" x="-13" y="-7" width="26" height="17" rx="1"/>
          <line class="icon" x1="-9" y1="-11" x2="-5" y2="-11"/>
          <line class="icon" x1="5" y1="-11" x2="9" y2="-11"/>
          <polyline class="icon" points="1,-3 -3,2 2,2 -2,7"/>
        </g>
        <text class="service-label" x="163" y="10" textLength="549" lengthAdjust="spacing">Batteries &amp; Diagnostics</text>
      </g>
      <g transform="translate(0,661)">
        <line class="leader" x1="9" y1="0" x2="90" y2="0"/>
        <use href="#hex-shape" x="113" class="hex"/>
        <g transform="translate(113,0)">
          <circle class="icon" cx="0" cy="0" r="13" stroke-width="3"/>
          <circle class="icon" cx="0" cy="0" r="5"/>
          <path class="icon" d="M-15,-6 A16,16 0 0 1 -6,-15"/>
        </g>
        <text class="service-label" x="163" y="10" textLength="408" lengthAdjust="spacing">Automotive Parts</text>
      </g>
      <g transform="translate(0,716)">
        <line class="leader" x1="9" y1="0" x2="90" y2="0"/>
        <use href="#hex-shape" x="113" class="hex"/>
        <g transform="translate(113,0)">
          <path class="icon-solid" d="M-14,-2 H4 V9 H-14 Z M5,1 H10 L14,5 V9 H5 Z"/>
          <circle class="icon-solid" cx="-9" cy="11" r="3"/>
          <circle class="icon-solid" cx="9" cy="11" r="3"/>
          <circle class="icon" cx="-4" cy="-11" r="6" stroke-width="1.8"/>
        </g>
        <text class="service-label" x="163" y="10" textLength="297" lengthAdjust="spacing">Vehicle Sales</text>
      </g>
    </g>

    <!-- lower bands -->
    <rect x="9" y="763" width="400" height="23" fill="var(--sign-grey)"/>
    <polygon points="392,786 425,754 698,754 761,685 869,685 869,786" fill="url(#red-sweep)"/>
    <polygon points="758,786 869,786 869,870 822,870" fill="url(#red-sweep)"/>

    <!-- contact -->
    <text class="contact-line" x="34" y="853" font-size="66" textLength="687" lengthAdjust="spacingAndGlyphs">48 Tamsin Road | 07 542 3917</text>
  </svg>
</main>
</body>
</html>
```